Great Opportunity !! Masters in Business Analytics College Course

the size is Full Page, with bleed*
8”x 10.75" plus 0.25" bleed.
please leave one inch for footer
the purpose is attract students to join this college program .
this is for students in USA .
college age of around 24 years old
I am looking for a flyer that is unique and shows creativity .
A flyer that people would want to look at it because it is unique.
you can choose either vector, text ,or picture.
if you do picture it should be a white USA citizen wearing a white solid shirt and not long hair

Target Market(s)

USA students about 23 in age to join this college program

Industry/Entity Type

education

Colors
0054AA
0677BA
7BADD7
CADEEF
E8F1F8
0094D4
00A9DD
6FCCEA
C7EBF8
E9F6FB

Requirements
Must have
• the text should not be crowded .. .. .. the ad should not be full of text
Should not have
• not have very large text .. it should not be a flyer that is full of text .. you have to figure out how to avoid looking at the ad and it is very busy with text

```html
<!DOCTYPE html>
<html lang="en">
<head>
<meta charset="utf-8">
<title>Masters Degree in Business Analytics Flyer</title>
<link href="https://fonts.googleapis.com/css2?family=Archivo:wght@300;400;500;600;700;800&display=swap" rel="stylesheet">
<style>
  :root {
    --stage: #a7a8ac;
    --paper: #f5e9e5;
    --orange: #ff4f00;
    --blue: #004da6;
    --blue-fold: #1b64b0;
    --green: #3deb8c;
    --blush: #f2d6d4;
    --panel: #fdf0ec;
    --pink: #f7bccd;
    --ink: #1c1c1c;
    --white: #f7f1ef;
  }
  * { margin: 0; padding: 0; box-sizing: border-box; }
  html, body { width: 893px; height: 1200px; overflow: hidden; }
  body {
    background: var(--stage);
    font-family: "Archivo", "Helvetica Neue", Arial, sans-serif;
    position: relative;
  }
  .flyer {
    position: absolute; left: 56px; top: 75px;
    width: 782px; height: 1050px;
    background: var(--paper);
  }
  .flyer > * { position: absolute; }
  .block-orange { left: 0; top: 0; width: 445px; height: 633px; background: var(--orange); }
  .block-green { left: 640px; top: 303px; width: 142px; height: 466px; background: var(--green); }
  .hero-photo {
    left: 80px; top: 48px; width: 652px; height: 585px;
    background: linear-gradient(100deg, #c99d74 0%, #b08c6c 25%, #7e93a8 45%, #e9e4de 70%, #f1ece6 100%);
  }
  .page-curl { left: 555px; top: 48px; width: 177px; height: 126px; }
  .title-shadow { left: 57px; top: 571px; width: 593px; height: 208px; background: var(--blush); }
  .title-box {
    left: 47px; top: 561px; width: 593px; height: 208px;
    background: var(--blue); padding: 0 27px;
  }
  .title-kicker {
    margin-top: 24px; color: var(--green);
    font-weight: 800; font-size: 22.5px; letter-spacing: 0.1px; white-space: nowrap;
  }
  .title-rule { margin-top: 13px; width: 539px; height: 2px; background: var(--green); }
  .title-main {
    margin-top: 18px; color: var(--white);
    font-size: 49px; line-height: 48px; white-space: nowrap;
  }
  .title-main .light { display: block; font-weight: 300; letter-spacing: 0.5px; }
  .title-main .bold { display: block; font-weight: 800; letter-spacing: -0.3px; }
  .intro {
    left: 47px; top: 790px; width: 450px;
    font-size: 14px; line-height: 19px; color: var(--ink); font-weight: 400;
  }
  .apply-shadow { left: 525px; top: 780px; width: 218px; height: 151px; background: var(--blush); }
  .apply-button {
    left: 515px; top: 770px; width: 218px; height: 49px;
    background: var(--orange); color: var(--white);
    display: flex; align-items: center; justify-content: space-between;
    padding: 0 14px;
    font-weight: 700; font-size: 24px;
  }
  .apply-list {
    left: 515px; top: 819px; width: 218px; height: 102px;
    background: var(--panel); list-style: none; padding: 13px 0 0 14px;
  }
  .apply-list li {
    display: flex; align-items: center; gap: 9px;
    font-size: 12.5px; font-weight: 600; line-height: 17.7px; color: var(--ink);
  }
  .footer {
    left: 47px; top: 958px; width: 686px; height: 63px;
    border: 1.5px solid var(--pink); display: flex;
  }
  .footer-logo {
    width: 189px; height: 100%; background: var(--pink);
    display: flex; align-items: center; justify-content: center;
    color: var(--white); font-weight: 700; font-size: 29px;
  }
</style>
</head>
<body>
  <main class="flyer">
    <div class="block-orange"></div>
    <div class="block-green"></div>
    <div class="hero-photo" role="img" aria-label="Photo of a smiling student in a denim jacket and white shirt holding a tablet in a bright campus hallway"></div>
    <svg class="page-curl" viewBox="0 0 177 126" aria-hidden="true">
      <path d="M0 0 H177 V126 Z" fill="var(--blue-fold)"/>
      <path d="M0 0 L177 126 C150 112 110 118 70 130 C55 90 40 35 0 0 Z" fill="var(--orange)"/>
    </svg>

    <div class="title-shadow"></div>
    <section class="title-box">
      <p class="title-kicker">PREPARE FOR A VERY IN DEMAND JOBS WITH A</p>
      <div class="title-rule"></div>
      <h1 class="title-main">
        <span class="light">MASTERS DEGREE IN</span>
        <span class="bold">BUSINESS ANALYTICS</span>
      </h1>
    </section>

    <p class="intro">Lorem ipsum dolor sit amet, consectetuer adipiscing elit, sed diam nonummy nibh euismod tincidunt ut laoreet dolore magna aliquam erat volutpat. Ut wisi enim ad minim veniam, quis nostrud exerci tation ullamcorper suscipit lobortis nisl ut aliquip.</p>

    <div class="apply-shadow"></div>
    <div class="apply-button">
      <span>APPLY NOW</span>
      <svg width="36" height="24" viewBox="0 0 36 24" aria-hidden="true">
        <path d="M1 12 H33 M23 2 L34 12 L23 22" fill="none" stroke="var(--blue)" stroke-width="2.5" stroke-linecap="round" stroke-linejoin="round"/>
      </svg>
    </div>
    <ul class="apply-list">
      <li><svg width="16" height="12" viewBox="0 0 16 12" aria-hidden="true"><path d="M1.5 6 L6 10.5 L14.5 1.5" fill="none" stroke="var(--orange)" stroke-width="2.6"/></svg>Bachelor's Degree</li>
      <li><svg width="16" height="12" viewBox="0 0 16 12" aria-hidden="true"><path d="M1.5 6 L6 10.5 L14.5 1.5" fill="none" stroke="var(--orange)" stroke-width="2.6"/></svg>Academic Transcripts</li>
      <li><svg width="16" height="12" viewBox="0 0 16 12" aria-hidden="true"><path d="M1.5 6 L6 10.5 L14.5 1.5" fill="none" stroke="var(--orange)" stroke-width="2.6"/></svg>Standardized Test Scores</li>
      <li><svg width="16" height="12" viewBox="0 0 16 12" aria-hidden="true"><path d="M1.5 6 L6 10.5 L14.5 1.5" fill="none" stroke="var(--orange)" stroke-width="2.6"/></svg>Work Experience (Optional)</li>
    </ul>

    <footer class="footer">
      <div class="footer-logo">LOGO</div>
    </footer>
  </main>
</body>
</html>
```